jewellery store flyer

Front to show
-company name and logo
underneath of company name, I want " The perfect creation" to be written.
-background bright tone jewellery or model wearing jewellery(prefer engagement and wedder or wedder set)

--------------------------------------------------------------
Back to show list of service and brief map of location
with addresss and contact detail

introducing newly established jewellery store with exclusive and unique jewellery. We offer you
-specialized in hand made jewellery
-on site jeweller and designer
-repair and restoring
-laser engraving and laser solder

4/31 Tarrawin Crescent Griffith ACT 2603
02) 6148 3072
Enquiry: marlow.k@postvane.com
---------------------------------------------------------------------
I have enclosed mockups that I made by myself, to show what I was thinking. this is just for reference. New flyer doesn't need to look the same.

I don't mind either holizontal nor vertical.
I don't mind if you add text or remove text that I have written above.
I want flyer to look morden and neat.

Good luck to you & me and enjoy creation.
Kind regards,
Pearl

Target Market(s)

introducing newly established store.
aiming for engagement & wedding rings and remakes

Industry/Entity Type

It Company

Font styles to use
Other font styles liked:
• Monotype corsive for script but name and address for SERIF

Colors

Designer to choose colors to be used in the design.

Requirements
Must have
• background photo including jewellery
• company name and address
• service detail
Nice to have
• brief map of location( I have red circled few places that people know more on the map I attached here.)
• Map to be simplified please.
• Please do not use Google map directly.
• Opening hours: Mon-Fri 9.30 to 5.30 Sat 10.00 to 5

```html
<!DOCTYPE html>
<html lang="en">
<head>
<meta charset="utf-8">
<title>Wrenfield Jewellery – Flyer Front and Back</title>
<link rel="stylesheet" href="https://fonts.googleapis.com/css2?family=Tinos:wght@400;700&display=swap">
<style>
  :root {
    --stage: #d6d6d6;
    --ink-white: #ffffff;
    --ink-dark: #111111;
    --band: #3a3a3a;
    --badge: #d9d9d9;
    --badge-ring: #2a2a2a;
    --badge-ink: #2a2a2a;
  }
  * { box-sizing: border-box; margin: 0; padding: 0; }
  html, body {
    width: 1200px; height: 1000px; overflow: hidden;
    background: var(--stage);
    font-family: "Tinos", "Times New Roman", serif;
  }
  .canvas { position: relative; width: 1200px; height: 1000px; }

  .flyer {
    position: absolute; top: 150px;
    width: 480px; height: 680px; overflow: hidden;
    box-shadow: 0 8px 24px rgba(0,0,0,.25);
  }
  .flyer svg.art { position: absolute; inset: 0; }
  .flyer--front { left: 90px; }
  .flyer--back  { left: 630px; }

  /* Front */
  .brand {
    position: absolute; left: 34px; top: 60px;
    display: flex; align-items: center; gap: 14px;
    color: var(--ink-white);
  }
  .brand__mark {
    width: 34px; height: 34px; border-radius: 50%;
    border: 2px solid var(--ink-white);
  }
  .brand__name {
    font-size: 30px; line-height: 1.05; letter-spacing: 2px;
    text-transform: uppercase; font-weight: 400;
  }
  .tagline {
    position: absolute; left: 0; top: 540px; width: 480px;
    text-align: right; padding-right: 30px;
    color: var(--ink-white); font-size: 40px;
    transform: rotate(-14deg); transform-origin: right center;
  }

  /* Back */
  .badge {
    position: absolute; width: 92px; height: 92px; border-radius: 50%;
    background: var(--badge); border: 4px solid var(--badge-ring);
    display: flex; align-items: flex-end; justify-content: center;
    padding-bottom: 22px;
    color: var(--badge-ink); font-size: 12px; letter-spacing: 1.5px;
    text-transform: uppercase;
  }
  .badge--platinum { left: 30px; top: 150px; }
  .badge--elegant  { left: 296px; top: 226px; }
  .badge--diamonds { left: 366px; top: 384px; }

  .intro {
    position: absolute; left: 30px; top: 262px; width: 250px;
    color: var(--ink-white); font-size: 17px; line-height: 1.3;
  }
  .intro p { margin-bottom: 4px; }
  .services { list-style: none; margin-top: 4px; }
  .services li::before { content: "-"; }

  .contact {
    position: absolute; left: 236px; top: 530px; width: 230px;
    color: var(--ink-white); font-size: 15px; line-height: 1.4;
    font-style: normal;
  }
</style>
</head>
<body>
<main class="canvas">

  <section class="flyer flyer--front" aria-label="Flyer front">
    <svg class="art" width="480" height="680" viewBox="0 0 480 680">
      <defs>
        <linearGradient id="frontPhoto" x1="0" y1="0" x2="1" y2="1">
          <stop offset="0" stop-color="#3b302e"/>
          <stop offset="0.45" stop-color="#b89f94"/>
          <stop offset="0.75" stop-color="#d9c8bf"/>
          <stop offset="1" stop-color="#6e5a55"/>
        </linearGradient>
      </defs>
      <rect width="480" height="680" fill="url(#frontPhoto)" role="img" aria-label="Photograph of a model wearing rings and bracelets"/>
      <g class="rings">
        <circle cx="0" cy="0" r="350" fill="#a5a5a5"/>
        <circle cx="0" cy="0" r="325" fill="#828282"/>
        <circle cx="0" cy="0" r="300" fill="#5e5e5e"/>
        <circle cx="0" cy="0" r="275" fill="#3a3a3a"/>
        <circle cx="0" cy="0" r="250" fill="#0d0d0d"/>
      </g>
      <polygon points="0,640 480,520 480,590 0,710" fill="#3a3a3a" opacity="0.92"/>
    </svg>
    <div class="brand">
      <span class="brand__mark"></span>
      <h1 class="brand__name">Wrenfield<br>Jewellery</h1>
    </div>
    <p class="tagline">The Perfect Creation</p>
  </section>

  <section class="flyer flyer--back" aria-label="Flyer back">
    <svg class="art" width="480" height="680" viewBox="0 0 480 680">
      <defs>
        <linearGradient id="backPhoto" x1="0" y1="0" x2="1" y2="1">
          <stop offset="0" stop-color="#9a9a9a"/>
          <stop offset="0.5" stop-color="#5c5c5c"/>
          <stop offset="1" stop-color="#2e2e2e"/>
        </linearGradient>
        <linearGradient id="housePhoto" x1="0" y1="0" x2="0" y2="1">
          <stop offset="0" stop-color="#cfcfcf"/>
          <stop offset="1" stop-color="#555555"/>
        </linearGradient>
      </defs>
      <rect width="480" height="680" fill="url(#backPhoto)" role="img" aria-label="Black and white photograph of a woman wearing a statement necklace"/>
      <polygon points="0,140 480,360 480,680 0,680" fill="#1e1e1e" opacity="0.6"/>
      <polygon points="0,120 0,260 180,190" fill="#2a2a2a" opacity="0.7"/>
      <rect x="30" y="530" width="190" height="130" fill="url(#housePhoto)" role="img" aria-label="Photograph of the store building"/>
    </svg>

    <div class="badge badge--platinum">Platinum</div>
    <div class="badge badge--elegant">Elegant</div>
    <div class="badge badge--diamonds">Diamonds</div>

    <div class="intro">
      <p>Introducing newly established jewellery store with exclusive and unique jewellery.</p>
      <p>We offer you:</p>
      <ul class="services">
        <li>Repair and restoring</li>
        <li>On site jeweller and designer</li>
        <li>Laser engraving and laser solder</li>
        <li>Specialized in hand made jewellery</li>
      </ul>
    </div>

    <address class="contact">
      4/31 Tarrawin Crescent<br>
      Griffith ACT 2603<br>
      T: 02) 6148 3072<br>
      Enquiry: marlow.k@postvane.com
    </address>
  </section>

</main>
</body>
</html>
```